Vor Mask business card

Create a new business card for Vor Mask. Black colour base front and back (the sides can be blue if that works) You can modify the blue colour to best suit the design. I am after a card that looks technical, modern and strong. one side with the Vor Mask and the other company details. The attached file has the details needed for the card. Flipside is the parent company name and needed but in a smaller size

Target Market(s)

Businesses (suppliers and customers)

Industry/Entity Type

Business

Contact Information for Business Card

Black colour base front and back

Font styles to use
Other font styles liked:
• attached

Requirements
Must have
• Logo's as attached

```html
<!DOCTYPE html>
<html lang="en">
<head>
<meta charset="utf-8">
<title>Vor Mask business card</title>
<link rel="stylesheet" href="https://fonts.googleapis.com/css2?family=Open+Sans:wght@400;600;700&family=Roboto+Condensed:wght@700&display=swap">
<style>
  :root {
    --canvas: #2b2e33;
    --card: #131417;
    --blue: #1e9be0;
    --white: #f2f4f6;
    --grey: #a9adb3;
    --silver: #c9ccd0;
    --rule: #8d9197;
  }
  * { box-sizing: border-box; margin: 0; padding: 0; }
  html, body { width: 1200px; height: 900px; overflow: hidden; }
  body {
    background: var(--canvas);
    font-family: "Open Sans", sans-serif;
    position: relative;
  }
  .card {
    position: absolute;
    top: 300px;
    width: 520px;
    height: 300px;
    background: var(--card);
    border-radius: 22px;
    overflow: hidden;
  }
  .card--front { left: 50px; }
  .card--back { left: 630px; }

  .wordmark {
    font-family: "Open Sans", sans-serif;
    font-weight: 700;
    color: var(--white);
    letter-spacing: 3px;
    line-height: 1;
    white-space: nowrap;
  }
  .tagline {
    font-weight: 600;
    color: var(--blue);
    text-transform: uppercase;
    letter-spacing: 5px;
    white-space: nowrap;
  }

  .card--front .wordmark { position: absolute; left: 34px; top: 30px; font-size: 44px; }
  .card--front .tagline { position: absolute; left: 36px; top: 82px; font-size: 13px; }

  .person { position: absolute; left: 36px; top: 122px; }
  .person__name {
    font-family: "Roboto Condensed", sans-serif;
    font-weight: 700;
    font-size: 22px;
    color: var(--blue);
    letter-spacing: 0.5px;
  }
  .person__role { font-size: 12px; color: var(--grey); }

  .divider {
    position: absolute;
    left: 36px; top: 180px;
    width: 400px; height: 1px;
    background: var(--rule);
  }

  .contacts { position: absolute; left: 36px; top: 192px; list-style: none; }
  .contacts li {
    display: flex; align-items: center; gap: 8px;
    font-size: 12.5px; color: var(--grey);
    line-height: 21px;
  }
  .contacts svg { width: 10px; height: 10px; fill: var(--blue); flex: none; }

  .address {
    position: absolute; left: 260px; top: 194px;
    display: flex; gap: 8px;
    font-size: 12.5px; color: var(--grey); line-height: 20px;
  }
  .address svg { width: 10px; height: 14px; fill: var(--blue); margin-top: 3px; flex: none; }

  .card--back { display: flex; flex-direction: column; align-items: center; justify-content: center; gap: 12px; }
  .card--back .wordmark { font-size: 60px; color: var(--silver); }
  .card--back .tagline { font-size: 15px; color: var(--grey); letter-spacing: 8px; }
</style>
</head>
<body>

<section class="card card--front" aria-label="Business card front">
  <div class="wordmark">VOR MASK</div>
  <div class="tagline">Built to endure</div>

  <div class="person">
    <div class="person__name">LENA HARWOOD</div>
    <div class="person__role">Managing Director</div>
  </div>

  <div class="divider"></div>

  <ul class="contacts">
    <li>
      <svg viewBox="0 0 10 10" aria-hidden="true"><path d="M2 0.5 L3.6 2.8 L2.7 3.8 Q3.8 6 6.2 7.3 L7.2 6.4 L9.5 8 L8.3 9.5 Q3.5 9 0.5 1.7 Z"/></svg>
      +61 400 555 018
    </li>
    <li>
      <svg viewBox="0 0 10 10" aria-hidden="true"><path d="M0.5 2 H9.5 V8 H0.5 Z M1.2 2.6 L5 5.4 L8.8 2.6 V3.4 L5 6.2 L1.2 3.4 Z" fill-rule="evenodd"/></svg>
      lena@northvaleint.com
    </li>
    <li>
      <svg viewBox="0 0 10 10" aria-hidden="true"><circle cx="5" cy="5" r="4.5"/></svg>
      www.northvaleint.com
    </li>
  </ul>

  <div class="address">
    <svg viewBox="0 0 10 14" aria-hidden="true"><path d="M5 0 A5 5 0 0 1 10 5 C10 8 5 14 5 14 C5 14 0 8 0 5 A5 5 0 0 1 5 0 Z M5 3 A2 2 0 1 0 5 7 A2 2 0 1 0 5 3 Z" fill-rule="evenodd"/></svg>
    <p>PO Box 120 Elmbrook,<br>S.A. 5099, Australia</p>
  </div>
</section>

<section class="card card--back" aria-label="Business card back">
  <div class="wordmark">VOR MASK</div>
  <div class="tagline">Built to endure</div>
</section>

</body>
</html>
```